Website for Life Strategies business

We need a website to present our video, audio and print content to subcribers at Vivid Horizon Mentors. We will offer a team of coaches who can help people breakthrough the barriers that keep them from reaching their physical, spiritual, financial, leadership and relationship goals.

Target Market(s)

Anyone who needs help with strategies to take their life to a new level of success.

Industry/Entity Type

Life Coaching

Logo Text

Vivid Horizon Mentors

Number of Pages Required

5+ page

Colors

Designer to choose colors to be used in the design.

Requirements
Must have
• The ability to present content as a package that includes Word Documents, videos and audio content as well as to be able to display books for sale. Each week their would be a new package for subscribers to access. It should provide the ability for subscribers to comment on the material and share how their lives were changed by the content. Should also include a shop page to offer merchandise for sale.
Nice to have
• Not sure
Should not have
• Not sure

```html
<!DOCTYPE html>
<html lang="en">
<head>
<meta charset="utf-8">
<title>Vivid Horizon Mentors</title>
<link href="https://fonts.googleapis.com/css2?family=Amaranth&family=Lato:wght@400;700&family=Montserrat:wght@400;600;700;800&family=Tinos&display=swap" rel="stylesheet">
<style>
:root{
  --ink:#111;
  --bar:#050505;
  --footer:#2b2b2b;
  --heading:#666;
  --body:#6f6f6f;
  --frame:#e4e4e4;
  --rule:#dcdcdc;
  --white:#fff;
  --button:#262626;
}
*{margin:0;padding:0;box-sizing:border-box}
html,body{width:1200px;height:2233px;overflow:hidden;background:var(--white)}
.page{position:relative;width:1200px;height:2233px;font-family:"Lato",sans-serif;color:var(--body)}
.abs{position:absolute}
.topbar{left:0;top:0;width:1200px;height:48px;background:var(--bar);color:var(--white);font:700 13px/48px "Lato",sans-serif}
.topbar .welcome{position:absolute;left:98px}
.topbar nav span{position:absolute;transform:translateX(-50%)}
.brand{left:0;top:70px;width:1200px;text-align:center;font:400 33px/44px "Amaranth",sans-serif;color:#333;letter-spacing:.5px}
.tagline{left:0;top:123px;width:1200px;text-align:center;font:400 12px/18px "Lato",sans-serif;color:#222}
.photo{display:block}
.hero{left:98px;top:161px;width:1004px;height:444px;background:linear-gradient(100deg,#9da6ad 0%,#b7bcc0 35%,#a59c95 60%,#c9bcb2 100%)}
.hero-title{left:98px;top:356px;width:1004px;text-align:center;font:700 37px/54px "Montserrat",sans-serif;color:var(--white);letter-spacing:1px}
.section-title{font:700 26px/34px "Montserrat",sans-serif;color:var(--heading);letter-spacing:.3px}
.body-copy{font:400 10.4px/20.8px "Lato",sans-serif;color:var(--body);text-align:justify}
.panel{border:8px solid var(--frame);background:var(--white);text-align:center}
.panel h3{font:700 20px/30px "Montserrat",sans-serif;color:var(--heading);letter-spacing:.5px}
.field{position:absolute;border:1px solid #ccc;height:28px;font:400 10px/26px "Lato",sans-serif;color:#999;text-align:left;padding-left:8px}
.btn{position:absolute;background:var(--ink);color:var(--white);font:800 19px/41px "Montserrat",sans-serif;text-align:center;letter-spacing:1px}
.player{position:absolute;left:20px;right:20px;top:205px;display:flex;justify-content:space-between;align-items:center;font:600 14px/20px "Montserrat",sans-serif;color:#555}
.player span{display:flex;align-items:center;gap:7px}
.rule{height:1px;background:var(--rule)}
.prompt{left:0;top:1745px;width:1200px;text-align:center;font:400 16px/24px "Tinos",serif;color:#444}
.cta{left:400px;top:1799px;width:379px;height:62px;background:var(--button);color:var(--white);font:500 17px/62px "Montserrat",sans-serif;text-align:center;letter-spacing:.5px}
.comments-label{left:73px;top:1897px;font:400 19px/24px "Montserrat",sans-serif;color:#888}
.comment-links{right:98px;top:1898px;font:400 15px/22px "Tinos",serif;color:#444;display:flex;gap:18px}
.comment-box{left:74px;top:1939px;width:1028px;height:172px;border:1px solid #e6e6e6}
.preview{left:902px;top:2077px;font:400 11px/16px "Tinos",serif;color:#555}
.post{left:954px;top:2068px;width:139px;height:34px;background:var(--button);color:var(--white);font:600 11px/34px "Montserrat",sans-serif;text-align:center;letter-spacing:.6px}
.footer{left:0;top:2177px;width:1200px;height:56px;background:var(--footer);color:var(--white);text-align:center;font:700 12px/56px "Montserrat",sans-serif}
</style>
</head>
<body>
<div class="page">
  <header class="abs topbar">
    <span class="welcome">Welcome To Vivid Horizon Mentors</span>
    <nav>
      <span style="left:752px">Home</span>
      <span style="left:822px">Pages</span>
      <span style="left:892px">Profile</span>
      <span style="left:973px">Subscribe</span>
      <span style="left:1070px">Newsletter</span>
    </nav>
  </header>

  <h1 class="abs brand">Vivid Horizon Mentors</h1>
  <p class="abs tagline">Physical, Spiritual, Financial, Leadership &amp; Relationship Goals</p>

  <div class="abs hero photo" role="img" aria-label="Photo of two women talking in a coaching session on a sofa"></div>
  <h2 class="abs hero-title">REFLECTIONS ON THE CREATIVE PATH</h2>

  <h2 class="abs section-title" style="left:98px;top:637px">OUR PURPOSE IS TO HELP YOU</h2>
  <div class="abs photo" role="img" aria-label="Photo of a coach with a notepad listening to a client on a sofa" style="left:98px;top:697px;width:627px;height:318px;background:linear-gradient(90deg,#d8d6d4 0%,#b9c9cf 30%,#d4d0cc 60%,#c9bba6 100%)"></div>
  <p class="abs body-copy" style="left:100px;top:1033px;width:630px">Lorem Ipsum is simply dummy text of the printing and typesetting industry. Lorem Ipsum has been the industry's standard dummy text ever since the 1500s, when an unknown printer took a galley of type and scrambled it to make a type specimen book. It has survived not only five centuries.Lorem Ipsum is simply dummy text of the printing and typesetting industry. Lorem Ipsum has been the industry's standard dummy text ever since the 1500s, when an unknown printer took a galley of type and scrambled it to make a type specimen book. It has survived not only five centuries</p>

  <h2 class="abs section-title" style="left:92px;top:1167px">MAKING IT EASIER TO REACH OUT</h2>
  <div class="abs photo" role="img" aria-label="Video still of a counsellor speaking with a client in a bright office" style="left:95px;top:1225px;width:627px;height:319px;background:linear-gradient(90deg,#8a8a86 0%,#a4a7a3 30%,#c8cbc4 55%,#a8ad9c 100%)"></div>
  <svg class="abs" style="left:389px;top:1367px" width="36" height="36" viewBox="0 0 36 36" aria-hidden="true">
    <circle cx="18" cy="18" r="15.5" fill="none" stroke="#fff" stroke-width="3"/>
    <path d="M14 11 L26 18 L14 25 Z" fill="#fff"/>
  </svg>
  <p class="abs body-copy" style="left:97px;top:1561px;width:630px">Lorem Ipsum is simply dummy text of the printing and typesetting industry. Lorem Ipsum has been the industry's standard dummy text ever since the 1500s, when an unknown printer took a galley of type and scrambled it to make a type specimen book. It has survived not only five centuries.Lorem Ipsum is simply dummy text of the printing and typesetting industry. Lorem Ipsum has been the industry's standard dummy text ever since the 1500s, when an unknown printer took a galley of type and scrambled it to make a type specimen book. It has survived not only five centuries</p>

  <aside>
    <section class="abs panel" style="left:789px;top:639px;width:310px;height:336px">
      <h3 style="margin-top:38px">SUBSCRIBE OUR<br>NEWSLETTER</h3>
      <p style="font:400 11.5px/16px 'Lato',sans-serif;color:#666;margin-top:12px">Get out latest update &amp; news</p>
      <div class="field" style="left:20px;top:144px;width:252px">Name *</div>
      <div class="field" style="left:20px;top:188px;width:252px">Email</div>
      <div class="btn" style="left:58px;top:240px;width:178px">SUBMIT</div>
    </section>

    <section class="abs panel" style="left:789px;top:1015px;width:310px;height:258px">
      <h3 style="margin-top:32px">LISTEN TO OUR<br>VOICE AND BE HAPPY</h3>
      <p style="font:400 11px/20px 'Lato',sans-serif;color:#666;margin:14px 18px 0;text-align:justify;text-align-last:center">Lorem Ipsum is simply dummy text of the printing and typesetting industry. Lorem Ipsum has been the industry's standard dummy text ever since the 1500s centuries.</p>
      <div class="player">
        <span><svg width="12" height="18" viewBox="0 0 12 18" aria-hidden="true"><rect x="3" y="0" width="6" height="11" rx="3" fill="#555"/><path d="M1 8 a5 5 0 0 0 10 0" fill="none" stroke="#555" stroke-width="1.6"/><path d="M6 13 V17 M3 17 H9" stroke="#555" stroke-width="1.6"/></svg>3.00</span>
        <span><svg width="18" height="18" viewBox="0 0 18 18" aria-hidden="true"><circle cx="9" cy="9" r="7.5" fill="none" stroke="#555" stroke-width="1.8"/><path d="M7 5.5 L12.5 9 L7 12.5 Z" fill="#555"/></svg>VOICE 1</span>
        <span style="gap:12px"><svg width="14" height="14" viewBox="0 0 14 14" aria-hidden="true"><path d="M1 5 H4 L8 1.5 V12.5 L4 9 H1 Z" fill="#555"/><path d="M10 4.5 Q12 7 10 9.5" fill="none" stroke="#555" stroke-width="1.3"/></svg><svg width="20" height="16" viewBox="0 0 20 16" aria-hidden="true"><rect x="0" y="12" width="2.5" height="4" fill="#555"/><rect x="4.5" y="9" width="2.5" height="7" fill="#555"/><rect x="9" y="6" width="2.5" height="10" fill="#555"/><rect x="13.5" y="3" width="2.5" height="13" fill="#555"/><rect x="18" y="0" width="2" height="16" fill="#555"/></svg></span>
      </div>
    </section>

    <div class="abs" style="left:789px;top:1318px;width:310px;height:335px;background:var(--frame)"></div>
    <div class="abs photo" role="img" aria-label="Illustration of a mental health poster on a grey board with health icons" style="left:799px;top:1326px;width:292px;height:320px;background:linear-gradient(180deg,#7b7f84 0%,#8d9196 45%,#9a8a86 70%,#b6aca3 100%)"></div>
  </aside>

  <div class="abs rule" style="left:79px;top:1715px;width:1024px"></div>
  <p class="abs prompt">Have you considered reaching out for help with something you're struggling with?</p>
  <div class="abs cta">DROP ME A LINE FOR HELP TODAY!</div>

  <div class="abs comments-label">Comments (0)</div>
  <div class="abs comment-links"><span>Newest First</span><span>Subscribe via e-mail</span></div>
  <div class="abs comment-box"></div>
  <span class="abs preview">Preview</span>
  <div class="abs post">POST COMMENT...</div>
  <div class="abs rule" style="left:74px;top:2141px;width:1028px"></div>

  <footer class="abs footer">© 2017 Vivid Horizon Mentors. All Rights Reserved.</footer>
</div>
</body>
</html>
```